All Out No Regrets Art

I'd like my motto "All Out No Regrets" made into art for my office. I'm in a very formal/conservative office building but my office is more modern and upbeat. Even though the motto sounds really bold and maybe even harsh, I'm looking for something upbeat and happy. Nothing too harsh/angular, I like swirls and modern whimsical things. Love the colors orange, gray and bright/lime green but it doesn't have to be just those colors or all those colors. I do NOT like navy blue and burgandy.
This needs to look like high-quality art, not like a "poster" because it's for an executive office.
I've updated the creative brief.

```html
<!DOCTYPE html>
<html lang="en">
<head>
<meta charset="UTF-8">
<title>All Out No Regrets</title>
<link rel="stylesheet" href="https://fonts.googleapis.com/css2?family=Bebas+Neue&family=Yellowtail&display=swap">
<style>
  :root {
    --amber-light: #f7bf0a;
    --amber-mid: #f0a800;
    --amber-deep: #e68f00;
    --lime: #d4ff0a;
    --lime-edge: #a8c400;
    --lime-shade: #7f8f00;
    --shadow: rgba(120, 70, 0, 0.45);
  }
  html, body {
    margin: 0;
    padding: 0;
    overflow: hidden;
  }
  .poster {
    position: relative;
    width: 848px;
    height: 1200px;
    overflow: hidden;
  }
  .backdrop {
    position: absolute;
    inset: 0;
    background:
      radial-gradient(ellipse at 50% 45%, var(--amber-light) 0%, var(--amber-mid) 55%, var(--amber-deep) 100%);
  }
  .word {
    position: absolute;
    margin: 0;
    line-height: 1;
    white-space: nowrap;
    color: var(--lime);
    transform-origin: center center;
    text-shadow:
      0 0 0 var(--lime),
      -2px -2px 0 var(--lime-edge),
      2px -2px 0 var(--lime-edge),
      -2px 2px 0 var(--lime-edge),
      2px 2px 0 var(--lime-edge),
      4px 5px 0 var(--lime-shade),
      7px 9px 10px var(--shadow);
  }
  .word--script {
    font-family: "Yellowtail", cursive;
    font-weight: 400;
  }
  .word--block {
    font-family: "Bebas Neue", sans-serif;
    font-weight: 400;
    letter-spacing: 4px;
  }
  .word--all {
    font-size: 250px;
    left: 190px;
    top: 60px;
    transform: rotate(22deg);
  }
  .word--out {
    font-size: 230px;
    left: 170px;
    top: 390px;
    transform: rotate(-70deg);
  }
  .word--no {
    font-size: 330px;
    left: 400px;
    top: 470px;
    transform: rotate(28deg);
  }
  .word--regrets {
    font-size: 205px;
    left: 50px;
    top: 770px;
    transform: rotate(31deg);
  }
</style>
</head>
<body>
  <main class="poster">
    <div class="backdrop" role="img" aria-label="Warm amber background with a faint geometric triangle pattern"></div>
    <h1 class="motto">
      <span class="word word--script word--all">All</span>
      <span class="word word--block word--out">OUT</span>
      <span class="word word--script word--no">No</span>
      <span class="word word--block word--regrets">REGRETS</span>
    </h1>
  </main>
</body>
</html>
```